Solar Advertising Flier to generate Biz

I need a advertisement that generates business to be used in a mailer for marketing purposes.

Im attaching a file that is a an idea of advertisement.
I do not want the "ZVN" specific information on it.
I want the background solar panels.
Same information as the ad.
And I've attached my Logo - I want the color scheme to match this.

Thank you

Target Market(s)

Middle to Upper Class Home Owners

Industry/Entity Type

Solar Energy

Requirements
Must have
• A call to action
• A professional look
Nice to have
• A family
• Great looking solar panels
Should not have
• Cartoons

```html
<!DOCTYPE html>
<html lang="en">
<head>
<meta charset="utf-8">
<title>Go Solar – Brightfield Energy Flier</title>
<link rel="stylesheet" href="https://fonts.googleapis.com/css2?family=Ubuntu:wght@400;500;700&family=Oswald:wght@500;600;700&family=Orbitron:wght@900&display=swap">
<style>
  :root {
    --backdrop: #e6e8ea;
    --blue: #1a8fd6;
    --blue-deep: #0f78c2;
    --blue-light: #3fb0ea;
    --title-blue: #1a7cc1;
    --green: #8dc63f;
    --green-bright: #9dcb3b;
    --grey-band: #c9c9c9;
    --ink: #333;
    --white: #fff;
  }
  * { margin: 0; padding: 0; box-sizing: border-box; }
  html, body { width: 1200px; height: 1200px; overflow: hidden; background: var(--backdrop); }
  .stage { position: relative; width: 1200px; height: 1200px; overflow: hidden; }
  .flier {
    position: absolute; left: 200px; top: 40px;
    width: 924px; height: 1294px;
    transform: scale(0.8655); transform-origin: top left;
    background: var(--white); overflow: hidden;
    box-shadow: 0 6px 24px rgba(0,0,0,.18);
    font-family: "Ubuntu", sans-serif;
  }
  .flier-shapes { position: absolute; inset: 0; }
  .brand { position: absolute; left: 655px; top: 48px; width: 220px; text-align: center; }
  .brand-dot { width: 100px; height: 100px; border-radius: 50%; border: 9px solid var(--title-blue); margin: 0 auto 14px; }
  .brand-name { font-family: "Ubuntu", sans-serif; font-weight: 500; color: var(--title-blue); font-size: 25px; letter-spacing: .5px; line-height: 1.05; }

  .badge-text { position: absolute; left: 485px; width: 260px; text-align: center; color: var(--white); white-space: nowrap; }
  .badge-lead { top: 424px; font-size: 19px; line-height: 24px; }
  .badge-amount { top: 462px; font-family: "Oswald", sans-serif; font-weight: 700; font-size: 98px; line-height: 110px; text-shadow: 2px 3px 0 rgba(0,0,0,.18); }
  .badge-rebate { top: 574px; font-weight: 500; font-size: 24px; display: flex; align-items: center; justify-content: center; gap: 4px; }
  .badge-rebate::before, .badge-rebate::after { content: ""; width: 26px; height: 1.5px; background: var(--white); margin-top: 14px; }
  .badge-terms { top: 610px; left: 525px; width: 180px; font-size: 8px; line-height: 10.5px; white-space: normal; }

  .headline-go { position: absolute; left: 74px; top: 520px; font-family: "Orbitron", sans-serif; font-weight: 900; font-size: 150px; line-height: 140px; color: var(--white); letter-spacing: 10px; }
  .headline-solar { position: absolute; left: 70px; top: 660px; font-family: "Oswald", sans-serif; font-weight: 600; font-size: 176px; line-height: 180px; color: var(--green-bright); letter-spacing: -3px; transform: scaleX(.8); transform-origin: left top; }

  .info-card { position: absolute; background: var(--white); border-radius: 18px; overflow: hidden; }
  .info-card-title { background: var(--grey-band); color: var(--title-blue); font-weight: 700; white-space: nowrap; }
  .card-easy { left: 62px; top: 853px; width: 444px; height: 229px; }
  .card-easy .info-card-title { height: 56px; font-size: 32px; line-height: 60px; padding-left: 25px; }
  .easy-list { list-style: none; padding: 12px 20px 0 30px; font-size: 17.5px; line-height: 22px; color: var(--ink); }
  .easy-list li { position: relative; padding-left: 18px; margin-bottom: 4px; }
  .easy-list li::before { content: ""; position: absolute; left: 0; top: 8px; width: 6px; height: 6px; border-radius: 50%; background: var(--blue); }
  .accent { color: var(--green); font-weight: 500; }

  .card-how { left: 535px; top: 874px; width: 338px; height: 205px; }
  .card-how .info-card-title { height: 50px; font-size: 26px; line-height: 56px; padding-left: 22px; }
  .how-copy { padding: 10px 20px 0 20px; font-size: 16px; line-height: 20px; color: var(--ink); text-align: justify; }

  .cta-line { position: absolute; left: 38px; top: 1112px; color: var(--white); font-weight: 500; font-size: 18px; white-space: nowrap; }
  .cta-line::after { content: ""; display: block; width: 250px; height: 2px; background: var(--white); margin-top: 4px; }
  .contact-band { position: absolute; left: 0; top: 1154px; width: 620px; height: 80px; background: linear-gradient(90deg, var(--green) 0%, var(--green) 55%, rgba(141,198,63,0) 100%); }
  .contact-phone { position: absolute; left: 33px; top: 1164px; display: flex; align-items: center; gap: 6px; color: var(--white); font-family: "Oswald", sans-serif; font-weight: 600; font-size: 38px; line-height: 60px; white-space: nowrap; }
  .contact-web { position: absolute; left: 300px; top: 1180px; display: flex; align-items: center; gap: 10px; color: var(--white); font-size: 20px; white-space: nowrap; }

  .photo-circle { position: absolute; border-radius: 50%; border: 5px solid var(--white); box-shadow: 0 4px 10px rgba(0,0,0,.2); }
  .photo-panels { left: 575px; top: 1101px; width: 154px; height: 154px; background: linear-gradient(180deg, #cfe6f7 0%, #8cc1ea 45%, #2f5f9e 70%, #a0896a 100%); }
  .photo-roof { left: 744px; top: 1139px; width: 108px; height: 108px; background: linear-gradient(160deg, #6db3ea 0%, #bcd9f1 35%, #2749b7 60%, #c7735a 100%); }
</style>
</head>
<body>
<div class="stage">
  <div class="flier">
    <svg class="flier-shapes" viewBox="0 0 924 1294" width="924" height="1294">
      <defs>
        <linearGradient id="panelPhoto" x1="0" y1="0" x2="1" y2="1">
          <stop offset="0" stop-color="#f4f8fb"/>
          <stop offset=".35" stop-color="#cfe3f1"/>
          <stop offset=".6" stop-color="#4f92c8"/>
          <stop offset="1" stop-color="#1c5f9c"/>
        </linearGradient>
        <linearGradient id="blueField" x1="0" y1="0" x2="0" y2="1">
          <stop offset="0" stop-color="#2a9fe2"/>
          <stop offset=".6" stop-color="#1a8fd6"/>
          <stop offset="1" stop-color="#1583d0"/>
        </linearGradient>
        <radialGradient id="badgeGreen" cx=".5" cy=".45" r=".6">
          <stop offset="0" stop-color="#9fd14c"/>
          <stop offset="1" stop-color="#7db533"/>
        </radialGradient>
      </defs>
      <rect width="924" height="1294" fill="#fff"/>
      <path role="img" aria-label="Photo of tilted solar panel arrays against a bright sky" d="M0 200 L190 35 L924 330 L924 520 L600 560 L0 520 Z" fill="url(#panelPhoto)" opacity=".9"/>
      <path d="M0 436 C170 385 420 370 580 420 L600 520 L0 540 Z" fill="var(--green)"/>
      <path d="M0 532 C170 470 400 445 560 472 L640 600 C740 640 850 720 924 800 L924 1294 L0 1294 Z" fill="#fff"/>
      <path d="M0 546 C170 484 400 460 560 486 L640 610 C740 650 850 730 924 812 L924 1294 L0 1294 Z" fill="url(#blueField)"/>
      <path d="M700 600 C790 640 860 700 890 735 C840 700 770 660 700 630 Z" fill="var(--green)"/>
      <circle cx="615" cy="536" r="165" fill="#fff"/>
      <circle cx="615" cy="536" r="152" fill="none" stroke="var(--blue)" stroke-width="3"/>
      <circle cx="615" cy="536" r="140" fill="url(#badgeGreen)"/>
      <path d="M493 566 A126 126 0 1 1 737 566" fill="none" stroke="#fff" stroke-width="4" stroke-linecap="round" stroke-dasharray="0 13"/>
    </svg>

    <div class="brand">
      <div class="brand-dot"></div>
      <div class="brand-name">BRIGHTFIELD ENERGY</div>
    </div>

    <div class="badge-text badge-lead">Call Today&amp;<br>Receive a</div>
    <div class="badge-text badge-amount">$500</div>
    <div class="badge-text badge-rebate">CASH REBATE</div>
    <div class="badge-text badge-terms">Limited time offer. Ad must be present at time of purchase. Call for details. Not valid with any other offer or on previous purchases.</div>

    <div class="headline-go">GO</div>
    <div class="headline-solar">SOLAR</div>

    <section class="info-card card-easy">
      <h2 class="info-card-title">WE MAKE IT EASY</h2>
      <ul class="easy-list">
        <li><span class="accent">$0 Down</span>, no upfront cost</li>
        <li><span class="accent">Save up to 90%</span> off your utility bill.</li>
        <li>Protect against inflation &amp; energy costs increases from your Utility Company.</li>
        <li>Provide clean, reliable energy for your family <span class="accent">powered by the sun</span></li>
      </ul>
    </section>

    <section class="info-card card-how">
      <h2 class="info-card-title">HOW IT WORKS</h2>
      <p class="how-copy">Your solar system allows you to <span class="accent">generate your own clean power</span> and COSTS LESS than your current utility company. Simply pay by the month, like you do now...but at a LOWER rate and <span class="accent">START SAVING IMMEDIATELY.</span></p>
    </section>

    <div class="cta-line">Call Today For A No Obligation Consultation</div>
    <div class="contact-band"></div>
    <div class="contact-phone">
      <svg width="22" height="22" viewBox="0 0 24 24" aria-hidden="true"><path d="M6.6 10.8a15 15 0 0 0 6.6 6.6l2.2-2.2c.3-.3.7-.4 1-.2 1.1.4 2.3.6 3.6.6.6 0 1 .4 1 1V20c0 .6-.4 1-1 1A17 17 0 0 1 3 4c0-.6.4-1 1-1h3.5c.6 0 1 .4 1 1 0 1.3.2 2.5.6 3.6.1.3 0 .7-.2 1z" fill="var(--blue)"/></svg>
      000-000-000
    </div>
    <div class="contact-web">
      <svg width="18" height="18" viewBox="0 0 20 20" aria-hidden="true"><circle cx="10" cy="10" r="8" fill="none" stroke="var(--blue)" stroke-width="2"/><path d="M2 10h16M10 2c3 3 3 13 0 16M10 2c-3 3-3 13 0 16" fill="none" stroke="var(--blue)" stroke-width="1.5"/></svg>
      your website goes here
    </div>

    <div class="photo-circle photo-panels" role="img" aria-label="Photo of a solar panel field under a cloudy sky"></div>
    <div class="photo-circle photo-roof" role="img" aria-label="Photo of solar panels on a tiled roof"></div>
  </div>
</div>
</body>
</html>
```